Need A Standard Musical Download Website

We are looking for a talented designer to create a unique web design for our startup Music website called Vorlen Music.
The website should be responsive and filled with some creative stuffs along with bright colors.

Vorlen music is a website loaded with different types of music and capable of downloading the requested music by its users.
There will be categories of music which would be sorted by the genre. They include RnB, Hip-Hop, Afro pop, Pop, Dancehall and Reggae).

DESIGN STYLE/THEME

Creative, trendy, colorful, unique, and easy to use. You have freedom of selecting which ever color suits you. The design must be energetic and attractive.

NAVIGATION

HOME-MUSIC(RnB, Hip hop, Afro pop, POP, dancehall, Reggae)-ARTISTE-NEWS-LOGIN

PAGES REQUIRED
------------
1)Home Page
2)Music

FONTS
GOOGLE FONTS is strongly recommended.

Designers can get inspiration from https://tunebarrowk.com

Industry/Entity Type

Startup

```html
<!DOCTYPE html>
<html lang="en">
<head>
<meta charset="utf-8">
<title>Vorlen Music</title>
<link rel="stylesheet" href="https://fonts.googleapis.com/css2?family=Oswald:wght@400;500&family=Open+Sans:wght@300;400&family=Roboto:wght@400;500;700&display=swap">
<style>
  :root {
    --orange: #ec6f16;
    --orange-dark: #d95d0a;
    --sky: #43b0e0;
    --sky-light: #52bce8;
    --ink: #111111;
    --text-gray: #8a8a8a;
    --heading-gray: #3a3a3a;
    --page: #fbfbfb;
    --footer: #f3f3f3;
    --icon-gray: #7a7a7a;
    --white: #ffffff;
  }
  * { box-sizing: border-box; margin: 0; padding: 0; }
  html, body { width: 1178px; height: 1200px; overflow: hidden; }
  body {
    background: var(--page);
    font-family: 'Open Sans', Arial, sans-serif;
    color: var(--ink);
    position: relative;
  }
  .page { position: relative; width: 1178px; height: 1200px; }

  /* Header brand */
  .brand {
    position: absolute; top: 16px; left: 0; width: 1178px;
    display: flex; justify-content: center; align-items: center; gap: 10px;
  }
  .brand-dot { width: 54px; height: 54px; border-radius: 50%; background: var(--orange); }
  .brand-name {
    font-family: 'Oswald', 'Arial Narrow', sans-serif;
    font-weight: 400; font-size: 42px; color: var(--ink); line-height: 1;
  }

  /* Navigation */
  .main-nav {
    position: absolute; top: 95px; left: 88px; width: 1004px; height: 48px;
    background: linear-gradient(var(--sky-light), var(--sky));
    display: flex;
  }
  .main-nav a {
    flex: 1; color: var(--white); text-decoration: none;
    font-family: 'Roboto', Arial, sans-serif; font-size: 16px;
    display: flex; align-items: center; justify-content: center;
  }
  .main-nav a.is-active {
    flex: 0 0 157px;
    background: linear-gradient(var(--orange), var(--orange-dark));
  }

  /* Hero */
  .hero {
    position: absolute; top: 144px; left: 88px; width: 1004px; height: 505px;
    box-shadow: 0 2px 6px rgba(0,0,0,0.25);
    overflow: hidden;
  }
  .hero-photo {
    position: absolute; left: 0; top: 0; width: 678px; height: 505px;
    background:
      radial-gradient(ellipse at 40% 35%, #e3c2a4 0%, rgba(227,194,164,0) 45%),
      linear-gradient(180deg, #cfc1aa 0%, #d9c8a8 45%, #cf5d6a 78%, #c94a5c 100%);
  }
  .hero-photo::after {
    content: ""; position: absolute; inset: 0;
    background: linear-gradient(90deg, rgba(90,60,40,0.35) 0%, rgba(0,0,0,0) 50%);
  }
  .hero-copy { position: absolute; left: 47px; top: 297px; z-index: 2; color: var(--white); }
  .hero-title {
    font-family: 'Oswald', 'Arial Narrow', sans-serif; font-weight: 500;
    font-size: 47px; line-height: 48px; text-shadow: 0 1px 3px rgba(0,0,0,0.3);
  }
  .hero-lines {
    margin-top: 4px; font-size: 17.5px; line-height: 28px;
    text-shadow: 0 1px 3px rgba(0,0,0,0.4);
  }
  .btn-download {
    display: flex; align-items: center; justify-content: center;
    margin-top: 17px; width: 175px; height: 43px; border-radius: 22px;
    background: var(--sky); color: var(--white);
    font-family: 'Roboto', Arial, sans-serif; font-size: 16px;
  }
  .slider-arrows { position: absolute; left: 586px; top: 450px; display: flex; gap: 7px; z-index: 2; }
  .slider-arrows span {
    width: 34px; height: 34px; border-radius: 50%;
    background: rgba(60,60,60,0.8);
    display: flex; align-items: center; justify-content: center;
  }

  /* Trial form */
  .trial {
    position: absolute; left: 678px; top: 0; width: 326px; height: 505px;
    background: linear-gradient(180deg, rgba(75,70,66,0.96), rgba(62,58,55,0.96));
  }
  .trial-title {
    position: absolute; top: 44px; left: 0; width: 326px; text-align: center;
    font-family: 'Oswald', 'Arial Narrow', sans-serif; font-weight: 400;
    font-size: 30px; color: var(--white); line-height: 1;
  }
  .field {
    position: absolute; left: 42px; width: 250px; height: 44px;
    background: var(--white); border: 1px solid #d6d6d6;
    font-family: 'Roboto', Arial, sans-serif; font-size: 12.5px; color: #222;
    display: flex; align-items: center; padding-left: 11px;
  }
  .field-select svg { position: absolute; right: 14px; top: 19px; }
  .opt-in {
    position: absolute; left: 43px; top: 310px;
    display: flex; align-items: center; gap: 7px;
    font-family: 'Roboto', Arial, sans-serif; font-size: 12.5px; color: var(--white);
  }
  .opt-in span.box { width: 13px; height: 13px; background: var(--white); border: 1px solid #bbb; }
  .btn-trial {
    position: absolute; left: 65px; top: 346px; width: 197px; height: 41px;
    border-radius: 21px; background: var(--orange); color: var(--white);
    font-family: 'Roboto', Arial, sans-serif; font-weight: 500; font-size: 16px;
    display: flex; align-items: center; justify-content: center;
  }
  .store-badge {
    position: absolute; top: 428px; width: 100px; height: 30px;
    background: #000; border: 1px solid #888; border-radius: 4px;
  }

  /* Genres */
  .genres { position: absolute; top: 660px; left: 88px; display: flex; gap: 8px; }
  .genre { position: relative; width: 194px; height: 174px; overflow: hidden; }
  .genre-label {
    position: absolute; left: 0; bottom: 0; width: 100%; height: 31px;
    background: rgba(10,10,10,0.72); color: var(--white);
    font-family: 'Roboto', Arial, sans-serif; font-weight: 700; font-size: 14px;
    display: flex; align-items: center; justify-content: center; gap: 4px;
  }
  .genre-rnb { background: linear-gradient(135deg, #0f6f84, #4fb8cf 55%, #0b4c5c); }
  .genre-hiphop { background: linear-gradient(135deg, #2f3a4a, #6b7a86 50%, #3a2f2a); }
  .genre-afropop { background: linear-gradient(160deg, #7a3b1a, #2a1d3a 55%, #3d2a5a); }
  .genre-dancehall { background: linear-gradient(160deg, #3a2a20, #a7876a 50%, #4a3a2c); }
  .genre-reggae { background: linear-gradient(180deg, #b8a794, #6a5645 55%, #2a1e16); }

  /* Welcome */
  .welcome { position: absolute; top: 885px; left: 0; width: 1178px; text-align: center; }
  .welcome h1 { font-weight: 300; font-size: 29px; color: var(--heading-gray); line-height: 1.2; }
  .welcome p {
    width: 880px; margin: 10px auto 0; font-weight: 300;
    font-size: 14.6px; line-height: 22.5px; color: var(--text-gray);
  }

  /* Footer */
  .site-footer {
    position: absolute; top: 1035px; left: 0; width: 1178px; height: 165px;
    background: var(--footer); text-align: center;
  }
  .footer-links {
    margin-top: 47px; font-family: 'Roboto', Arial, sans-serif; font-size: 12.5px;
    color: var(--ink); display: flex; justify-content: center; gap: 12px;
  }
  .social { margin-top: 22px; display: flex; justify-content: center; gap: 20px; }
  .social span { width: 21px; height: 21px; border-radius: 50%; background: var(--icon-gray); }
  .copyright { margin-top: 13px; font-family: 'Roboto', Arial, sans-serif; font-size: 12.5px; color: #222; }
</style>
</head>
<body>
<div class="page">

  <header class="brand">
    <span class="brand-dot"></span>
    <span class="brand-name">VORLEN MUSIC</span>
  </header>

  <nav class="main-nav">
    <a href="#" class="is-active">HOME</a>
    <a href="#">MUSIC</a>
    <a href="#">ARTISTE</a>
    <a href="#">NEWS</a>
    <a href="#">LOGIN</a>
  </nav>

  <section class="hero">
    <div class="hero-photo" role="img" aria-label="Young woman in a striped top listening to music on headphones, eyes closed"></div>
    <div class="hero-copy">
      <div class="hero-title">VORLEN MUSIC</div>
      <div class="hero-lines">Free unlimited 50% off new music to fill it<br>Download up to 25 free songs with trial</div>
      <div class="btn-download">DOWNLOAD NOW</div>
    </div>
    <div class="slider-arrows">
      <span><svg width="12" height="16" viewBox="0 0 12 16"><path d="M9 2 L3 8 L9 14" fill="none" stroke="#fff" stroke-width="2.4"/></svg></span>
      <span><svg width="12" height="16" viewBox="0 0 12 16"><path d="M3 2 L9 8 L3 14" fill="none" stroke="#fff" stroke-width="2.4"/></svg></span>
    </div>

    <form class="trial">
      <div class="trial-title">START YOUR TRIAL</div>
      <div class="field" style="top:99px">Email Address</div>
      <div class="field" style="top:150px">Password</div>
      <div class="field" style="top:202px">Re-Enter Password</div>
      <div class="field field-select" style="top:253px">Country
        <svg width="10" height="6" viewBox="0 0 10 6"><path d="M0 0 H10 L5 6 Z" fill="#111"/></svg>
      </div>
      <label class="opt-in"><span class="box"></span>Email me about new &amp; free Music</label>
      <div class="btn-trial">START YOUR TRIAL</div>
      <span class="store-badge" style="left:57px"></span>
      <span class="store-badge" style="left:167px"></span>
    </form>
  </section>

  <section class="genres">
    <div class="genre genre-rnb" role="img" aria-label="Studio microphone with headphones on a blue sound-wave background">
      <div class="genre-label">RNB <svg width="13" height="13" viewBox="0 0 13 13"><circle cx="6.5" cy="6.5" r="6.5" fill="#fff"/><path d="M5 3.5 L8 6.5 L5 9.5" fill="none" stroke="#111" stroke-width="1.8"/></svg></div>
    </div>
    <div class="genre genre-hiphop" role="img" aria-label="Hip hop performer in a hoodie with glowing light effects">
      <div class="genre-label">HIP HOP <svg width="13" height="13" viewBox="0 0 13 13"><circle cx="6.5" cy="6.5" r="6.5" fill="#fff"/><path d="M5 3.5 L8 6.5 L5 9.5" fill="none" stroke="#111" stroke-width="1.8"/></svg></div>
    </div>
    <div class="genre genre-afropop" role="img" aria-label="DJ hand on a mixing console with a turntable">
      <div class="genre-label">AFRO POP <svg width="13" height="13" viewBox="0 0 13 13"><circle cx="6.5" cy="6.5" r="6.5" fill="#fff"/><path d="M5 3.5 L8 6.5 L5 9.5" fill="none" stroke="#111" stroke-width="1.8"/></svg></div>
    </div>
    <div class="genre genre-dancehall" role="img" aria-label="Dancer with headphones in a city street scene">
      <div class="genre-label">DANCEHALL <svg width="13" height="13" viewBox="0 0 13 13"><circle cx="6.5" cy="6.5" r="6.5" fill="#fff"/><path d="M5 3.5 L8 6.5 L5 9.5" fill="none" stroke="#111" stroke-width="1.8"/></svg></div>
    </div>
    <div class="genre genre-reggae" role="img" aria-label="Concert crowd with raised hands under stage lights">
      <div class="genre-label">REGGAE <svg width="13" height="13" viewBox="0 0 13 13"><circle cx="6.5" cy="6.5" r="6.5" fill="#fff"/><path d="M5 3.5 L8 6.5 L5 9.5" fill="none" stroke="#111" stroke-width="1.8"/></svg></div>
    </div>
  </section>

  <section class="welcome">
    <h1>WELCOME TO VORLEN MUSIC</h1>
    <p>It is a long established fact that a reader will be distracted by the readable content of a page when looking at its layout. The point of using Lorem Ipsum is that it has a more-or-less normal distribution of letters, as opposed to using 'Content here, content here', making it look like readable English. Many desktop publishing packages and web page editors now use Lorem Ipsum</p>
  </section>

  <footer class="site-footer">
    <div class="footer-links">
      <span>ABOUT</span><span>|</span><span>PRIVACY</span><span>|</span><span>TERMS</span><span>|</span><span>LEGAL</span><span>|</span><span>CONTACT</span>
    </div>
    <div class="social">
      <span></span><span></span><span></span><span></span><span></span><span></span><span></span><span></span>
    </div>
    <div class="copyright">Copyright © 2017&nbsp; All Rights Reserved</div>
  </footer>

</div>
</body>
</html>
```